Landscape Contractor in need of New Web Design

HELP.. Please Help!!!!. Our current website is old, outdated, ugly... and well nothing like us.... so we are looking for someone to help build a new website that fits our company direction. We are a landscape company with multiple locations in order to meet the needs of our clients and their projects throughout the midwest. When most people think of landscaping, they think of mowing grandmas yard, but that is NOT even remotely close to what we do. We are 100% a commercial landscape company meaning we complete landscape and irrigation services for large scale commercial projects. We are looking for a website to showcase our commercial talents and awesome team of people.
Updates

Address of current website is www.plovermeadowco.com

```html
<!DOCTYPE html>
<html lang="en">
<head>
<meta charset="utf-8">
<title>Plover Meadow – Landscape &amp; Irrigation</title>
<link href="https://fonts.googleapis.com/css2?family=Baloo+2:wght@400;500;600;700;800&family=Hind:wght@400;500;600&display=swap" rel="stylesheet">
<style>
:root{
  --lime:#a4f21b;
  --lime-soft:#e3fbb3;
  --forest:#2c4a1f;
  --forest-deep:#1f3d1a;
  --ink:#1d1d1d;
  --text:#4a4a4a;
  --white:#ffffff;
  --card-line:#e4e4e4;
  --paper:#f4f5f2;
  --black:#000000;
  --star:#f7a81b;
}
*{box-sizing:border-box;margin:0;padding:0}
html,body{width:1200px;height:3348px;overflow:hidden}
body{position:relative;background:var(--white);font-family:"Hind",sans-serif;color:var(--text)}
.abs{position:absolute}
.heading{font-family:"Baloo 2",sans-serif}

/* hero */
.hero{position:absolute;left:0;top:0;width:1200px;height:700px}
.hero-photo{position:absolute;inset:0;background:linear-gradient(160deg,#3a4036 0%,#4d5a44 35%,#2c3328 70%,#1f241c 100%)}
.hero-photo::after{content:"";position:absolute;inset:0;background:rgba(0,0,0,.35)}
.brand{position:absolute;display:flex;align-items:center;gap:10px;font-family:"Baloo 2",sans-serif;font-weight:700;color:var(--lime)}
.brand-dot{border-radius:50%;background:var(--lime)}
.topbar{position:absolute;top:28px;left:477px;display:flex;align-items:center;gap:14px;font-family:"Baloo 2",sans-serif;font-size:14px;color:var(--white);font-weight:500}
.topbar .sep{width:1px;height:20px;background:rgba(255,255,255,.5)}
.social{width:24px;height:24px;border:1.5px solid var(--white);border-radius:50%}
.nav-rule{position:absolute;left:348px;top:68px;width:741px;height:1px;background:rgba(255,255,255,.45)}
.nav-rule::before{content:"";position:absolute;left:20px;top:-1px;width:20px;height:3px;background:var(--lime)}
.nav{position:absolute;top:86px;left:348px;display:flex;font-family:"Baloo 2",sans-serif;font-size:14px;color:var(--white);font-weight:500;letter-spacing:.4px}
.nav span{display:block}
.apply{position:absolute;left:973px;top:80px;width:116px;height:33px;background:rgba(255,255,255,.18);border:1px solid rgba(255,255,255,.35);color:var(--white);font-family:"Baloo 2",sans-serif;font-size:14px;display:flex;align-items:center;justify-content:center;gap:8px}
.hero-kicker{position:absolute;top:222px;width:1200px;text-align:center;font-size:37px;color:var(--white);font-weight:500}
.hero-line{position:absolute;left:338px;top:296px;width:523px;height:1px;background:var(--lime)}
.hero-title{position:absolute;top:312px;width:1200px;text-align:center;font-size:50px;color:var(--white);font-weight:500}
.btn{position:absolute;display:flex;align-items:center;justify-content:center;gap:8px;font-family:"Baloo 2",sans-serif;font-weight:600;font-size:16px;border-radius:14px 0 14px 0}
.btn-solid{background:var(--lime);color:var(--forest-deep)}
.btn-line{border:2px solid var(--lime);color:var(--white)}
.dot{position:absolute;top:561px;width:12px;height:12px;border:1.5px solid var(--white);border-radius:50%}

/* services */
.section-title{position:absolute;width:1200px;text-align:center;font-size:42px;font-weight:700;color:var(--forest);letter-spacing:.5px}
.halo{position:absolute;left:298px;top:904px;width:604px;height:600px;border-radius:50%;background:var(--lime-soft)}
.card{position:absolute;width:300px;height:296px;background:var(--white);border:1px solid var(--card-line);box-shadow:0 2px 10px rgba(0,0,0,.08);text-align:center}
.card.active{border:2px solid var(--forest)}
.card-icon{position:absolute;left:119px;top:32px;width:62px;height:62px;border-radius:50%;background:#cfd7cc}
.card h3{position:absolute;top:118px;width:100%;font-family:"Baloo 2",sans-serif;font-size:20px;font-weight:600;color:var(--ink)}
.card p{position:absolute;top:160px;left:30px;width:240px;font-size:14.5px;line-height:26px;color:var(--text)}

/* why */
.why{position:absolute;left:0;top:1569px;width:1200px;height:606px;background:linear-gradient(90deg,#24461b 0%,#3b6f20 45%,#7cc51b 80%,#a4f21b 100%)}
.why h2{position:absolute;left:112px;top:80px;font-size:38px;font-weight:700;color:var(--white);letter-spacing:1px}
.why p{position:absolute;left:112px;top:150px;width:440px;font-size:14.5px;line-height:26px;color:var(--white)}
.checks{position:absolute;left:112px;top:254px;list-style:none}
.checks li{display:flex;align-items:center;gap:14px;height:45px;font-family:"Baloo 2",sans-serif;font-size:19px;font-weight:600;color:var(--white)}
.why-photo{position:absolute;left:604px;top:89px;width:484px;height:429px;background:linear-gradient(135deg,#4d7a2c 0%,#6a8f3e 30%,#2f4a3a 60%,#1e90b8 85%,#3a4e2a 100%);box-shadow:0 10px 30px rgba(0,0,0,.3)}

/* testimonials */
.testi{position:absolute;left:0;top:2175px;width:1200px;height:760px;background:var(--paper)}
.quote-card{position:absolute;left:112px;top:2374px;width:421px;height:447px;background:var(--white);border:1px solid var(--card-line);box-shadow:0 3px 14px rgba(0,0,0,.08);text-align:center}
.avatar{position:absolute;left:175px;top:32px;width:70px;height:70px;border-radius:50%;background:#f08a8a}
.quote-card blockquote{position:absolute;left:40px;top:128px;width:341px;font-size:14.5px;line-height:27.5px;color:var(--ink)}
.quote-card .name{position:absolute;top:340px;width:100%;font-family:"Baloo 2",sans-serif;font-size:19px;font-weight:600;color:var(--ink);letter-spacing:.5px}
.stars{position:absolute;top:372px;left:148px;display:flex;gap:8px}
.stat{position:absolute;width:255px;height:95px;background:var(--white);border:1px solid var(--card-line);display:flex;align-items:center;gap:16px;padding-left:14px}
.stat-badge{width:62px;height:62px;border-radius:50%;background:var(--lime-soft);flex:none;display:flex;align-items:center;justify-content:center}
.stat-badge i{display:block;width:30px;height:30px;border-radius:50%;background:#f7b52b}
.stat b{display:block;font-family:"Baloo 2",sans-serif;font-size:19px;font-weight:600;color:var(--ink);line-height:24px}
.stat small{display:block;font-family:"Baloo 2",sans-serif;font-size:14px;font-weight:500;color:var(--ink)}

/* footer */
.footer{position:absolute;left:0;top:2925px;width:1200px;height:423px;background:var(--black);color:var(--white)}
.footer h4{position:absolute;top:110px;font-family:"Baloo 2",sans-serif;font-size:20px;font-weight:600;color:var(--lime)}
.footer h4::after{content:"";position:absolute;left:0;top:34px;width:140px;height:3px;background:linear-gradient(90deg,var(--lime),rgba(164,242,27,0))}
.footer .about{position:absolute;left:112px;top:187px;width:270px;font-size:14.5px;line-height:26px}
.footer .copy{position:absolute;left:112px;top:336px;font-size:11px;font-weight:500}
.links{position:absolute;left:446px;top:170px;list-style:none;font-size:14.5px}
.links li{height:41.5px}
.contact-item{position:absolute;left:634px;display:flex;gap:12px;font-size:14.5px;line-height:21px;width:195px}
.contact-rule{position:absolute;left:634px;width:195px;height:1px;background:rgba(255,255,255,.4)}
.field{position:absolute;left:879px;width:207px;border:1px solid var(--white);font-size:11px;padding:4px 6px}
.send{position:absolute;left:879px;top:313px;width:207px;height:39px;background:var(--lime);color:var(--black);font-family:"Baloo 2",sans-serif;font-weight:700;font-size:17px;display:flex;align-items:center;justify-content:center}
</style>
</head>
<body>

<!-- Hero -->
<header class="hero">
  <div class="hero-photo" role="img" aria-label="Landscaper laying turf beside a curved paver walkway"></div>

  <div class="brand" style="left:114px;top:40px;font-size:24px;">
    <span class="brand-dot" style="width:34px;height:34px;"></span>Plover Meadow
  </div>

  <div class="topbar">
    <span>Talk To Us Today!</span>
    <svg width="24" height="24" viewBox="0 0 24 24" fill="none" stroke="#fff" stroke-width="1.5"><circle cx="12" cy="12" r="11"/><path d="M8.5 7.5l2 2-1 1.5c.8 1.5 2 2.7 3.5 3.5l1.5-1 2 2-1.2 1.4c-3.5-.4-7.3-4.2-7.7-7.7z"/></svg>
    <span>(785) 555-0148</span>
    <svg width="14" height="14" viewBox="0 0 14 14" fill="none" stroke="#fff" stroke-width="1.5"><circle cx="6" cy="6" r="4.5"/><path d="M9.5 9.5L13 13"/></svg>
    <span class="sep"></span>
    <svg width="22" height="22" viewBox="0 0 22 22" fill="none" stroke="#fff" stroke-width="1.4"><circle cx="11" cy="11" r="10"/><circle cx="11" cy="9" r="3.5"/><path d="M4.5 17.5c1.5-2.5 3.8-3.5 6.5-3.5s5 1 6.5 3.5"/></svg>
    <span>My Account</span>
    <span class="sep"></span>
    <span class="social"></span><span class="social"></span><span class="social"></span>
  </div>

  <div class="nav-rule"></div>
  <nav class="nav">
    <span style="width:115px">HOME</span>
    <span style="width:138px">SERVICES</span>
    <span style="width:143px">ABOUT US</span>
    <span style="width:138px">GALLERY</span>
    <span>CONTACT</span>
  </nav>
  <div class="apply">
    <svg width="16" height="16" viewBox="0 0 16 16" fill="none" stroke="#fff" stroke-width="1.4"><path d="M9 2h5v12H9M2 8h8M7 5l3 3-3 3"/></svg>Apply Now!
  </div>

  <div class="hero-kicker heading">Welcome to Plover Meadow</div>
  <div class="hero-line"></div>
  <h1 class="hero-title heading">15 yrs of Professional Landscaping</h1>

  <div class="btn btn-solid" style="left:442px;top:397px;width:155px;height:47px;">More About Us <span style="font-size:10px">▸</span></div>
  <div class="btn btn-line" style="left:638px;top:397px;width:120px;height:47px;">Learn More</div>

  <span class="dot" style="left:566px"></span>
  <span class="dot" style="left:591px;width:18px;height:18px;top:558px;border-color:var(--lime);background:radial-gradient(circle,var(--lime) 0 4px,transparent 5px)"></span>
  <span class="dot" style="left:622px"></span>

  <svg class="abs" style="left:0;top:540px" width="1200" height="160" viewBox="0 0 1200 160">
    <path d="M0 120 C200 132 380 150 560 118 C720 90 820 25 960 28 C1080 30 1150 80 1200 128 L1200 160 L0 160Z" fill="#fff"/>
    <path d="M440 140 C500 138 530 130 560 118 C720 90 820 25 960 28 C1080 30 1150 80 1200 128" fill="none" stroke="#a4f21b" stroke-width="6"/>
  </svg>
</header>

<!-- Services -->
<h2 class="section-title heading" style="top:734px">Services We Provide</h2>
<div class="halo"></div>

<article class="card" style="left:112px;top:842px">
  <span class="card-icon" role="img" aria-label="Sprout and trowel icon"></span>
  <h3>Maintenance</h3>
  <p>I am text block. Click edit button to change this text. Lorem ipsum dolor sit amet, consectetur adipisg elit, dapibus leo.</p>
</article>
<article class="card" style="left:448px;top:844px">
  <span class="card-icon" role="img" aria-label="Fertilizer bag icon"></span>
  <h3>Chemical Applications</h3>
  <p>I am text block. Click edit button to change this text. Lorem ipsum dolor sit amet, consectetur adipisg elit, dapibus leo.</p>
</article>
<article class="card active" style="left:785px;top:842px">
  <span class="card-icon" style="background:#c9f27a" role="img" aria-label="Grass with butterflies icon"></span>
  <h3>Turf Management</h3>
  <p>I am text block. Click edit button to change this text. Lorem ipsum dolor sit amet, consectetur adipisg elit, dapibus leo.</p>
</article>
<article class="card" style="left:112px;top:1178px">
  <span class="card-icon" role="img" aria-label="Tree icon"></span>
  <h3>Hardscaping</h3>
  <p>I am text block. Click edit button to change this text. Lorem ipsum dolor sit amet, consectetur adipisg elit, dapibus leo.</p>
</article>
<article class="card" style="left:448px;top:1180px">
  <span class="card-icon" role="img" aria-label="Sprinkler icon"></span>
  <h3>Irrigation</h3>
  <p>I am text block. Click edit button to change this text. Lorem ipsum dolor sit amet, consectetur adipisg elit, dapibus leo.</p>
</article>
<article class="card" style="left:785px;top:1176px">
  <span class="card-icon" role="img" aria-label="Trees and shrubs icon"></span>
  <h3>Landscaping</h3>
  <p>I am text block. Click edit button to change this text. Lorem ipsum dolor sit amet, consectetur adipisg elit, dapibus leo.</p>
</article>

<!-- Why choose us -->
<section class="why">
  <h2 class="heading">Why Choose Us?</h2>
  <p>Our company's dedication to innovative design projects created some of the most distinguished landscape projects throughout Kansas, Missouri, and Oklahoma.</p>
  <ul class="checks">
    <li><svg width="26" height="20" viewBox="0 0 26 20" fill="none" stroke="#fff" stroke-width="3.5" stroke-linecap="round"><path d="M2 10l7 7L24 2"/></svg>Licensed &amp; Insured</li>
    <li><svg width="26" height="20" viewBox="0 0 26 20" fill="none" stroke="#fff" stroke-width="3.5" stroke-linecap="round"><path d="M2 10l7 7L24 2"/></svg>Dependable Services</li>
    <li><svg width="26" height="20" viewBox="0 0 26 20" fill="none" stroke="#fff" stroke-width="3.5" stroke-linecap="round"><path d="M2 10l7 7L24 2"/></svg>Specialized Company</li>
    <li><svg width="26" height="20" viewBox="0 0 26 20" fill="none" stroke="#fff" stroke-width="3.5" stroke-linecap="round"><path d="M2 10l7 7L24 2"/></svg>Free Consultations &amp; Day Sceheling</li>
  </ul>
  <div class="btn btn-solid" style="left:112px;top:456px;width:130px;height:49px;">Learn More <span style="font-size:10px">▸</span></div>
  <div class="why-photo" role="img" aria-label="Gardener in a cap planting shrubs along drip irrigation line"></div>
</section>

<!-- Testimonials -->
<section class="testi"></section>
<h2 class="section-title heading" style="top:2253px">Testimonials</h2>

<span class="abs" style="left:526px;top:2466px;width:36px;height:44px;border-radius:0 22px 22px 0;background:var(--forest)"></span>
<span class="abs" style="left:526px;top:2736px;width:30px;height:34px;border-radius:0 17px 17px 0;background:var(--forest)"></span>
<span class="abs" style="left:86px;top:2770px;width:66px;height:66px;border-radius:50%;background:var(--lime)"></span>

<div class="quote-card">
  <span class="avatar" role="img" aria-label="Customer portrait"></span>
  <blockquote>"At vero eos et accusamus et iusto odio dignissimos ducimus qui blanditiis praesentium voluptatum deleniti atque corrupti quos dolores et quas molestias excepturi sint occaecati cupiditate non provident, similique sunt in culpa qui officia deserunt mollitia animi, id est laborum et dolorum fuga."</blockquote>
  <div class="name">DANA WHITFIELD</div>
  <div class="stars">
    <svg width="18" height="18" viewBox="0 0 24 24"><path d="M12 2l3 7 7 .6-5.4 4.7 1.7 7.2L12 17.8 5.7 21.5l1.7-7.2L2 9.6 9 9z" fill="#f7a81b"/></svg>
    <svg width="18" height="18" viewBox="0 0 24 24"><path d="M12 2l3 7 7 .6-5.4 4.7 1.7 7.2L12 17.8 5.7 21.5l1.7-7.2L2 9.6 9 9z" fill="#f7a81b"/></svg>
    <svg width="18" height="18" viewBox="0 0 24 24"><path d="M12 2l3 7 7 .6-5.4 4.7 1.7 7.2L12 17.8 5.7 21.5l1.7-7.2L2 9.6 9 9z" fill="#f7a81b"/></svg>
    <svg width="18" height="18" viewBox="0 0 24 24"><path d="M12 2l3 7 7 .6-5.4 4.7 1.7 7.2L12 17.8 5.7 21.5l1.7-7.2L2 9.6 9 9z" fill="#f7a81b"/></svg>
    <svg width="18" height="18" viewBox="0 0 24 24"><path d="M12 2l3 7 7 .6-5.4 4.7 1.7 7.2L12 17.8 5.7 21.5l1.7-7.2L2 9.6 9 9z" fill="#f7a81b"/></svg>
  </div>
</div>

<div class="stat" style="left:833px;top:2444px">
  <span class="stat-badge" role="img" aria-label="Thumbs up icon"><i style="background:#3a86d8"></i></span>
  <div><b>5 out of 5</b><small>Rated</small></div>
</div>
<div class="stat" style="left:611px;top:2508px">
  <span class="stat-badge" role="img" aria-label="Trophy icon"><i></i></span>
  <div><b>100%</b><small>Professional Services</small></div>
</div>
<div class="stat" style="left:762px;top:2591px">
  <span class="stat-badge" role="img" aria-label="Award ribbon icon"><i style="background:#f0592b"></i></span>
  <div><b>Top Rated</b><small>Award</small></div>
</div>

<svg class="abs" style="left:44px;top:2572px" width="24" height="32" viewBox="0 0 24 32" fill="none" stroke="#1d1d1d" stroke-width="2.5"><path d="M18 3L6 16l12 13"/></svg>
<svg class="abs" style="left:1130px;top:2572px" width="24" height="32" viewBox="0 0 24 32" fill="none" stroke="#1d1d1d" stroke-width="2.5"><path d="M6 3l12 13L6 29"/></svg>

<svg class="abs" style="left:0;top:2860px" width="1200" height="70" viewBox="0 0 1200 70">
  <path d="M0 20 C150 40 260 110 420 90 C600 70 700 0 900 10 C1030 18 1120 40 1200 30 L1200 70 L0 70Z" fill="#000"/>
</svg>

<!-- Footer -->
<footer class="footer">
  <div class="brand" style="left:112px;top:120px;font-size:21px;">
    <span class="brand-dot" style="width:30px;height:30px;"></span>Plover Meadow
  </div>
  <p class="about">Plover Meadow strives to set the standard for the highest quality lawn &amp; landscape products and services and to exceed our customer's expectations every time.</p>
  <div class="copy">Copyrights 2021 &nbsp;|&nbsp; Rights Reserved</div>

  <h4 style="left:445px">QUICK LINKS</h4>
  <ul class="links">
    <li>Home</li><li>About us</li><li>Services</li><li>Testimonials</li><li>Contact us</li>
  </ul>

  <h4 style="left:633px">CONTACT US</h4>
  <div class="contact-item" style="top:178px">
    <svg width="18" height="20" viewBox="0 0 18 20" fill="none" stroke="#fff" stroke-width="1.4"><path d="M9 19s6-6 6-11A6 6 0 003 8c0 5 6 11 6 11z"/><circle cx="9" cy="8" r="2.2"/></svg>
    <span>PLOVER MEADOW CO.<br>4120 W Meadowlark Lane<br>Shawnee, KS 66299</span>
  </div>
  <div class="contact-rule" style="top:258px"></div>
  <div class="contact-item" style="top:270px">
    <svg width="16" height="14" viewBox="0 0 16 14" fill="none" stroke="#fff" stroke-width="1.3"><rect x="1" y="2" width="14" height="10"/><path d="M1 2l7 6 7-6"/></svg>
    <span>hello@plovermeadowco.com</span>
  </div>
  <div class="contact-rule" style="top:301px"></div>
  <div class="contact-item" style="top:315px">
    <svg width="16" height="16" viewBox="0 0 24 24" fill="none" stroke="#fff" stroke-width="1.6"><path d="M6 3l4 4-2 2.5c1.3 2.6 3.5 4.8 6.5 6.5L17 14l4 4-2.2 2.5C11.5 20 4 12.5 3.5 5.2z"/></svg>
    <span>1-913-555-0172</span>
  </div>
  <div class="contact-rule" style="top:344px"></div>

  <h4 style="left:879px">CONTACT FORM</h4>
  <div class="field" style="top:166px;height:30px">Full Name</div>
  <div class="field" style="top:209px;height:28px">Email</div>
  <div class="field" style="top:250px;height:50px">Message</div>
  <div class="send">SEND</div>
</footer>

</body>
</html>
```